Prepare a modern, professional business card for Bramford Ledger Services (BLS) Our company is in the banking, compliance and finance industry. We provide kiosks, software integration, and compliance guidelines so that banks can "bank" Marijuana Dispensaries with TrevMon, Office of Halvern Affairs and NTRB approval.

Target Market(s)

Banks

Industry/Entity Type

Business

Contact Information for Business Card

Owen R Pelley
Bramford Ledger Services
Vice President
742 Quarry Ridge Road
Suite 310
Las Vegas, NV 89135
owen@bramfordls.net
702-555-0147

Font styles to use
Sans Serif

Requirements
Nice to have
• I like the clean simple appearance of Quillon computers. Perhaps the three LETTERS of BLS can be the LOGO on the Card and the Company name could be incorporated in the contact information. Like colors of white, black and gray

```html
<!DOCTYPE html>
<html lang="en">
<head>
<meta charset="utf-8">
<title>Bramford Ledger Services – Business Card</title>
<link rel="stylesheet" href="https://fonts.googleapis.com/css2?family=Open+Sans:wght@400;600;700&display=swap">
<style>
  :root {
    --page-bg: #d9d9d9;
    --card-gray: #8a8a8a;
    --panel-white: #ffffff;
    --edge-black: #111111;
    --ink-dark: #3b3b3b;
    --ink-mid: #6d6d6d;
    --ink-light: #f4f4f4;
  }
  html, body {
    margin: 0;
    width: 1200px;
    height: 1000px;
    overflow: hidden;
    background: var(--page-bg);
    font-family: "Open Sans", sans-serif;
  }
  .card {
    position: absolute;
    left: 150px;
    top: 240px;
    width: 900px;
    height: 520px;
    border-radius: 40px;
    overflow: hidden;
    background: var(--card-gray);
    box-shadow: 0 6px 18px rgba(0,0,0,0.18);
  }
  .card-shapes { position: absolute; inset: 0; }
  .brand {
    position: absolute;
    left: 440px;
    top: 70px;
    width: 400px;
    text-align: center;
  }
  .brand-mark {
    font-size: 96px;
    font-weight: 700;
    color: var(--ink-mid);
    letter-spacing: 6px;
    line-height: 1;
  }
  .brand-name {
    margin-top: 14px;
    font-size: 17px;
    font-weight: 700;
    color: var(--ink-mid);
    letter-spacing: 2px;
    text-transform: uppercase;
  }
  .contact {
    position: absolute;
    left: 62px;
    top: 276px;
    color: var(--ink-light);
  }
  .contact-name { font-size: 22px; font-weight: 600; color: var(--ink-dark); margin: 0; }
  .contact-title { font-size: 17px; margin: 0 0 30px 16px; color: var(--ink-light); }
  .contact-line {
    display: flex;
    align-items: center;
    gap: 8px;
    font-size: 18px;
    margin: 2px 0;
  }
  .contact-line svg { width: 16px; height: 16px; flex: none; }
  .contact-address { font-size: 23px; font-weight: 700; line-height: 1.2; }
  .contact-indent { padding-left: 24px; }
</style>
</head>
<body>
  <div class="card">
    <svg class="card-shapes" viewBox="0 0 900 520" aria-hidden="true">
      <polygon points="0,28 878,28 878,452 868,452 868,36 0,36" fill="var(--edge-black)"/>
      <polygon points="200,36 868,36 868,448" fill="var(--panel-white)"/>
    </svg>

    <div class="brand">
      <div class="brand-mark">BLS</div>
      <div class="brand-name">Bramford Ledger Services</div>
    </div>

    <div class="contact">
      <p class="contact-name">Owen R Pelley</p>
      <p class="contact-title">Vice President</p>
      <div class="contact-line contact-address">
        <svg viewBox="0 0 16 16"><path d="M8 1a5 5 0 0 0-5 5c0 4 5 9 5 9s5-5 5-9a5 5 0 0 0-5-5zm0 7a2 2 0 1 1 0-4 2 2 0 0 1 0 4z" fill="var(--ink-dark)"/></svg>
        <span>742 Quarry Ridge Road</span>
      </div>
      <div class="contact-line contact-address contact-indent">Suite 310 Las Vegas.</div>
      <div class="contact-line">
        <svg viewBox="0 0 16 16"><rect x="1" y="3" width="14" height="10" fill="var(--ink-dark)"/><path d="M1 3l7 6 7-6" stroke="var(--ink-light)" stroke-width="1.2" fill="none"/></svg>
        <span>NV 89135 owen@bramfordls.net</span>
      </div>
      <div class="contact-line">
        <svg viewBox="0 0 16 16"><circle cx="8" cy="8" r="7" fill="none" stroke="var(--ink-dark)" stroke-width="1.6"/><path d="M5.5 4.5l1.5 1.5-1 1c.6 1.3 1.7 2.4 3 3l1-1 1.5 1.5-1 1.2c-2.8-.4-5.3-2.9-5.7-5.7z" fill="var(--ink-dark)"/></svg>
        <span>702-555-0147</span>
      </div>
    </div>
  </div>
</body>
</html>
```